Business Card Design Project

I am a Chiropractor that is looking for a new business card.  Our logo was slightly changed lately, therefore need a new, more professional look.
We are a modern, non-stuffy chiropractic office.  Want a contemporary look that will let people know this is not your typical doctors office.  Our logo is red, and contains the name of our business: realign.  The u in the logo is green, stressing the most important part of our business: "u"

Target Market(s)
moderate to upper income bracket, family friendly
www.realignspine.example
Gordon Pell
Family Chiropractor
412 Birch Ave
Millbrook, TX 78650
512.555.0147 phone
512.555.0148 fax
Industry/Entity Type
Business
Requirements
Must have
- www.realignspine.example
Gordon Pell
Family Chiropractor
412 Birch Ave
Millbrook, TX 78650
512.555.0147 phone
512.555.0148 fax

```html
<!DOCTYPE html>
<html lang="en">
<head>
<meta charset="utf-8">
<title>realign business card</title>
<link href="https://fonts.googleapis.com/css2?family=Questrial&family=Arimo:wght@400;700&display=swap" rel="stylesheet">
<style>
  :root {
    --page: #ffffff;
    --card: #ffffff;
    --brand-red: #ee3f37;
    --band-red: #b34a44;
    --band-green: #6db543;
    --text-light: #ffffff;
    --shadow: rgba(0, 0, 0, 0.35);
  }
  * { margin: 0; padding: 0; box-sizing: border-box; }
  html, body { width: 1200px; height: 901px; overflow: hidden; background: var(--page); }
  .canvas { position: relative; width: 1200px; height: 901px; }
  .card {
    position: absolute; left: 295px; width: 612px; height: 349px;
    background: var(--card); overflow: hidden;
    box-shadow: 3px 4px 6px var(--shadow);
  }
  .card--front { top: 62px; }
  .card--back { top: 496px; }
  .card__bands { position: absolute; inset: 0; width: 612px; height: 349px; }
  .wordmark {
    position: absolute; left: 0; width: 612px; text-align: center;
    font-family: "Questrial", sans-serif; font-size: 72px; line-height: 1;
    color: var(--brand-red); letter-spacing: 1px;
  }
  .card--front .wordmark { top: 112px; }
  .card--back .wordmark { top: 74px; }
  .web {
    position: absolute; font-family: "Arimo", sans-serif; font-size: 18px;
    color: var(--text-light);
  }
  .card--front .web { top: 311px; left: 0; width: 612px; text-align: center; }
  .identity {
    position: absolute; right: 355px; top: 241px; text-align: right;
    font-family: "Arimo", sans-serif; color: var(--text-light);
  }
  .identity__name { font-size: 19px; font-weight: 700; color: var(--band-green); line-height: 22px; }
  .identity__role { font-size: 17px; line-height: 20px; }
  .identity .web { position: static; display: block; margin-top: 20px; font-size: 18px; }
  .divider {
    position: absolute; left: 305px; top: 246px; width: 1px; height: 82px;
    background: linear-gradient(to bottom, rgba(255,255,255,0), rgba(255,255,255,0.9), rgba(255,255,255,0));
  }
  .contact {
    position: absolute; left: 367px; top: 243px;
    font-family: "Arimo", sans-serif; font-size: 17px; line-height: 21px; color: var(--text-light);
    list-style: none;
  }
  .contact__icon { display: inline-block; width: 15px; height: 13px; vertical-align: -1px; margin-right: 5px; }
</style>
</head>
<body>
<div class="canvas">

  <section class="card card--front">
    <svg class="card__bands" viewBox="0 0 612 349" aria-hidden="true">
      <path d="M0 233 Q306 347 612 233 L612 349 L0 349 Z" fill="var(--band-green)"/>
      <path d="M0 260 Q306 340 612 260 L612 349 L0 349 Z" fill="var(--band-red)"/>
    </svg>
    <div class="wordmark">realign</div>
    <div class="web">www.realignspine.example</div>
  </section>

  <section class="card card--back">
    <svg class="card__bands" viewBox="0 0 612 349" aria-hidden="true">
      <path d="M0 121 Q306 287 612 121 L612 349 L0 349 Z" fill="var(--band-green)"/>
      <path d="M0 166 Q306 286 612 166 L612 349 L0 349 Z" fill="var(--band-red)"/>
    </svg>
    <div class="wordmark">realign</div>

    <div class="identity">
      <div class="identity__name">Gordon Pell</div>
      <div class="identity__role">Family Chiropractor</div>
      <span class="web">www.realignspine.example</span>
    </div>

    <div class="divider"></div>

    <ul class="contact">
      <li>412 Birch Ave</li>
      <li>Millbrook, TX 78650</li>
      <li>
        <svg class="contact__icon" viewBox="0 0 14 12" aria-label="phone">
          <path d="M1 4 Q7 0 13 4 L11 6 L9 4.5 L5 4.5 L3 6 Z" fill="var(--band-green)"/>
          <rect x="3" y="6" width="8" height="5" rx="1" fill="var(--band-green)"/>
        </svg>512.555.0147
      </li>
      <li>
        <svg class="contact__icon" viewBox="0 0 14 12" aria-label="fax">
          <rect x="4" y="0" width="6" height="3" fill="var(--band-green)"/>
          <rect x="1" y="3.5" width="12" height="5" rx="1" fill="var(--band-green)"/>
          <rect x="4" y="8" width="6" height="4" fill="var(--band-green)"/>
        </svg>512.555.0148
      </li>
    </ul>
  </section>

</div>
</body>
</html>
```